Proposal Template Design

We are looking to have our proposal templates redesigned. attached are examples of what we have been using. as well as our current logo

```html
<!DOCTYPE html>
<html lang="en">
<head>
<meta charset="utf-8">
<title>Ridgeline Insulation – Proposal Template</title>
<link rel="stylesheet" href="https://fonts.googleapis.com/css2?family=Open+Sans:wdth,wght@75..100,300..800&display=swap">
<style>
  :root{
    --backdrop:#8a8b8a;
    --paper:#ffffff;
    --brand-blue:#1b5fab;
    --brand-dark:#030f1b;
    --accent-light:#5fa9de;
    --ink:#111111;
    --body-ink:#3a3a3a;
    --rule:#bfbfbf;
  }
  *{margin:0;padding:0;box-sizing:border-box}
  html,body{width:1003px;height:1200px;overflow:hidden}
  body{background:var(--backdrop);position:relative;font-family:"Open Sans",Arial,sans-serif;color:var(--body-ink)}
  .page{position:absolute;width:398px;height:515px;background:var(--paper);overflow:hidden}
  .page--cover{left:88px;top:62px}
  .page--about{left:516px;top:62px}
  .page--scope{left:88px;top:622px}
  .page--pricing{left:516px;top:622px}

  .header{position:absolute;left:0;top:0;width:398px;height:86px}
  .header__art{position:absolute;left:0;top:0}
  .brand{position:absolute;left:28px;top:30px;display:flex;align-items:center;gap:5px;
    font-weight:800;font-stretch:75%;font-size:17px;color:var(--brand-dark);letter-spacing:.2px}
  .brand__mark{width:11px;height:11px;background:var(--brand-blue)}
  .brand-bar{position:absolute;left:28px;top:69px;width:140px;height:7px}
  .nav{position:absolute;left:217px;top:68px;width:156px;display:flex;justify-content:space-between;
    font-stretch:75%;font-weight:600;font-size:7.6px;color:var(--brand-dark);white-space:nowrap}
  .nav span.sep{color:var(--brand-blue)}
  .page--cover .nav{color:var(--brand-blue)}
  .header-contact{position:absolute;left:249px;top:14px;font-stretch:75%;font-weight:600;font-size:7.4px;
    color:var(--accent-light);line-height:11.6px}
  .contact-line{display:flex;align-items:center;gap:6px}
  .icon{width:7px;height:7px;flex:none}

  .cover-title{position:absolute;left:47px;top:222px;font-stretch:75%;font-weight:700;color:var(--brand-blue);
    font-size:40px;line-height:40px;letter-spacing:.3px}
  .cover-date{position:absolute;left:48px;top:304px;font-stretch:75%;font-weight:700;color:var(--ink);font-size:21px}
  .cover-contact{position:absolute;left:160px;top:461px;font-stretch:75%;font-weight:700;color:var(--ink);
    font-size:10.6px;line-height:12.8px}
  .cover-contact .contact-line{gap:9px}

  .photo{position:absolute;left:0;top:86px;width:398px;height:200px;
    background:linear-gradient(115deg,#d9dcdc 0%,#eeebdd 35%,#e3dcc3 60%,#8e8877 78%,#c9cccc 100%)}
  .section-title{position:absolute;left:28px;font-stretch:75%;font-weight:700;color:var(--brand-blue);font-size:17px}
  .body-copy{font-size:7.6px;line-height:10.7px;color:var(--body-ink)}
  .body-copy p+p{margin-top:8px}
  .about-copy{position:absolute;left:28px;top:328px;width:345px}
  .columns{position:absolute;left:28px;top:109px;width:344px;display:grid;grid-template-columns:166px 167px;column-gap:11px}
  .footer-band{position:absolute;left:0;bottom:0;width:398px;height:9px;background:var(--brand-blue)}

  .timeline{position:absolute;left:28px;top:334px;width:343px;border-collapse:collapse;font-size:6.2px;line-height:9px}
  .timeline th{background:var(--brand-blue);color:#fff;font-weight:700;font-size:7.4px;height:14px;
    border:1px solid #fff;border-top:0;letter-spacing:.3px}
  .timeline td{border:1px solid var(--rule);vertical-align:top;padding:2px 6px 4px;height:33px;color:var(--body-ink)}
  .timeline td.date{padding-left:5px}

  .pricing{position:absolute;left:28px;top:131px;width:342px}
  .pricing__head{height:21px;background:var(--brand-blue);color:#fff;font-size:6.6px;font-weight:700;position:relative}
  .pricing__head span,.pricing__row span{position:absolute;top:50%;transform:translateY(-50%)}
  .pricing__rows{margin-left:19px;width:306px}
  .pricing__row{position:relative;border-bottom:1px solid var(--rule);font-size:6.4px;color:#444}
  .pricing__row--item{height:25.7px}
  .pricing__row--sum{height:20.6px}
  .c-desc{left:22px}.c-qty{left:136px}.c-price{left:189px}.c-total{left:256px}
  .pricing__row .c-desc{left:3px}.pricing__row .c-qty{left:117px}.pricing__row .c-price{left:170px}.pricing__row .c-total{left:237px}
  .pricing__row--grand{font-weight:700;color:var(--ink);height:23px}
</style>
</head>
<body>

<svg width="0" height="0" style="position:absolute" aria-hidden="true">
  <defs>
    <linearGradient id="band" x1="0" y1="0" x2="1" y2="0">
      <stop offset="0" stop-color="#1b5fab"/><stop offset=".55" stop-color="#0b2d52"/><stop offset="1" stop-color="#020b15"/>
    </linearGradient>
    <linearGradient id="wedge" x1="1" y1="0" x2=".4" y2="1">
      <stop offset="0" stop-color="#020b15"/><stop offset=".45" stop-color="#124a88"/><stop offset="1" stop-color="#1b63b2"/>
    </linearGradient>
    <linearGradient id="corner" x1="0" y1="0" x2=".6" y2="1">
      <stop offset="0" stop-color="#1b63b2"/><stop offset="1" stop-color="#020b15"/>
    </linearGradient>
    <linearGradient id="barfill" x1="0" y1="0" x2="1" y2="0">
      <stop offset="0" stop-color="#62b0e5"/><stop offset="1" stop-color="#1b5fab"/>
    </linearGradient>
    <symbol id="i-pin" viewBox="0 0 10 10"><circle cx="5" cy="5" r="5" fill="currentColor"/><circle cx="5" cy="4.3" r="1.6" fill="#fff"/><path d="M3.4 5 5 7.8 6.6 5Z" fill="#fff"/></symbol>
    <symbol id="i-phone" viewBox="0 0 10 10"><circle cx="5" cy="5" r="5" fill="currentColor"/><path d="M3.2 2.8c.5-.4.9-.3 1.1.2l.3.8c.1.3 0 .5-.3.7.3.7.8 1.2 1.5 1.5.2-.3.4-.4.7-.3l.8.3c.5.2.6.6.2 1.1-1.8 1.4-5.5-2.4-4.3-4.3Z" fill="#fff"/></symbol>
    <symbol id="i-mail" viewBox="0 0 10 10"><circle cx="5" cy="5" r="5" fill="currentColor"/><rect x="2.6" y="3.3" width="4.8" height="3.4" fill="#fff"/><path d="M2.6 3.3 5 5.2 7.4 3.3" stroke="currentColor" stroke-width=".6" fill="none"/></symbol>
  </defs>
</svg>

<!-- Cover -->
<section class="page page--cover">
  <svg class="header__art" width="398" height="515" aria-hidden="true">
    <polygon points="155,0 398,0 398,63 198,63" fill="url(#band)"/>
    <polygon points="184,42 212,85 169,85" fill="#1b5fab"/>
    <line x1="0" y1="85.5" x2="398" y2="85.5" stroke="var(--accent-light)" stroke-width="1"/>
    <polygon points="212,86 398,86 398,356" fill="url(#wedge)"/>
    <polygon points="0,368 102,515 0,515" fill="#1b5fab"/>
    <polygon points="0,430 69,515 0,515" fill="url(#corner)"/>
  </svg>
  <div class="brand"><span class="brand__mark"></span>Ridgeline Insulation</div>
  <nav class="nav"><span>SPRAY FOAM</span><span class="sep">|</span><span>FIBERGLASS</span><span class="sep">|</span><span>INSULATION</span><span class="sep">|</span><span>ROOFING</span></nav>
  <h1 class="cover-title">FINAL<br>PROJECT PROPOSAL</h1>
  <p class="cover-date">September 2022</p>
  <div class="cover-contact" style="color:var(--ink)">
    <div class="contact-line"><svg class="icon" style="color:var(--brand-blue)"><use href="#i-pin"/></svg>P.O Box 482, Lakeside Texas 75990</div>
    <div class="contact-line"><svg class="icon" style="color:var(--brand-blue)"><use href="#i-phone"/></svg>555-018-2740</div>
    <div class="contact-line"><svg class="icon" style="color:var(--brand-blue)"><use href="#i-mail"/></svg>@ridgelinefoam.com</div>
  </div>
</section>

<!-- About -->
<section class="page page--about">
  <svg class="header__art" width="398" height="86" aria-hidden="true">
    <polygon points="155,0 398,0 398,63 198,63" fill="url(#band)"/>
    <polygon points="184,42 212,85 169,85" fill="#1b5fab"/>
    <line x1="0" y1="85.5" x2="398" y2="85.5" stroke="var(--accent-light)" stroke-width="1"/>
  </svg>
  <div class="brand"><span class="brand__mark"></span>Ridgeline Insulation</div>
  <svg class="brand-bar" width="140" height="7" aria-hidden="true"><polygon points="0,0 140,0 137,7 0,7" fill="url(#barfill)"/></svg>
  <div class="header-contact">
    <div class="contact-line"><svg class="icon" style="color:var(--accent-light)"><use href="#i-pin"/></svg>P.O Box 482, Lakeside Texas 75990</div>
    <div class="contact-line"><svg class="icon" style="color:var(--accent-light)"><use href="#i-phone"/></svg>555-018-2740</div>
    <div class="contact-line"><svg class="icon" style="color:var(--accent-light)"><use href="#i-mail"/></svg>@ridgelinefoam.com</div>
  </div>
  <nav class="nav"><span>SPRAY FOAM</span><span class="sep">|</span><span>FIBERGLASS</span><span class="sep">|</span><span>INSULATION</span><span class="sep">|</span><span>ROOFING</span></nav>
  <div class="photo" role="img" aria-label="Installer in white protective suit spraying foam insulation between attic rafters"></div>
  <h2 class="section-title" style="top:298px">About Us</h2>
  <div class="body-copy about-copy">
    <p>Lorem ipsum dolor sit amet, consectetur adipiscing elit. Praesent ut lobortis est, at laoreet leo. Aliquam posuere placerat elementum. Pellentesque et ornare risus. Vestibulum blandit arcu nisi, elementum blandit elit facilisis a. Duis molestie malesuada condimentum. Proin auctor blandit diam vestibulum dapibus. Proin laoreet pellentesque felis, at fermentum neque sagittis ut. Duis gravida est vitae purus mollis laoreet.</p>
    <p>Pellentesque sagittis auctor sapien, vel rhoncus libero commodo et. Nullam in imperdiet ligula, eu mollis erat. In hac habitasse platea dictumst. Aliquam ligula mi, posuere vitae sem ut, vestibulum commodo dui. Integer commodo, metus vehicula laoreet interdum, odio felis condimentum metus, in pretium sem risus quis arcu. In eget nisl tempus arcu scelerisque pulvinar et sit amet magna. Lorem ipsum dolor sit amet, consectetur adipiscing elit. Praesent turpis neque, tincidunt vel ante vel, pellentesque porttitor dui. Maecenas pellentesque commodo elit et iaculis.</p>
  </div>
  <div class="footer-band"></div>
</section>

<!-- Scope & Timeline -->
<section class="page page--scope">
  <svg class="header__art" width="398" height="86" aria-hidden="true">
    <polygon points="155,0 398,0 398,63 198,63" fill="url(#band)"/>
    <polygon points="184,42 212,85 169,85" fill="#1b5fab"/>
    <line x1="0" y1="85.5" x2="398" y2="85.5" stroke="var(--accent-light)" stroke-width="1"/>
  </svg>
  <div class="brand"><span class="brand__mark"></span>Ridgeline Insulation</div>
  <svg class="brand-bar" width="140" height="7" aria-hidden="true"><polygon points="0,0 140,0 137,7 0,7" fill="url(#barfill)"/></svg>
  <div class="header-contact">
    <div class="contact-line"><svg class="icon" style="color:var(--accent-light)"><use href="#i-pin"/></svg>P.O Box 482, Lakeside Texas 75990</div>
    <div class="contact-line"><svg class="icon" style="color:var(--accent-light)"><use href="#i-phone"/></svg>555-018-2740</div>
    <div class="contact-line"><svg class="icon" style="color:var(--accent-light)"><use href="#i-mail"/></svg>@ridgelinefoam.com</div>
  </div>
  <nav class="nav"><span>SPRAY FOAM</span><span class="sep">|</span><span>FIBERGLASS</span><span class="sep">|</span><span>INSULATION</span><span class="sep">|</span><span>ROOFING</span></nav>
  <div class="body-copy columns">
    <div>
      <p>Nulla varius eros suscipit, sodales metus at, pretium ipsum. Donec vulputate, justo eget vestibulum fringilla, tellus diam varius dui, ac rhoncus ante velit eu dolor. Vestibulum eget urna in elit dignissim luctus vel et nunc. Proin erat orci, iaculis eget nunc in, hendrerit egestas metus.</p>
      <p>Duis molestie sagittis metus sed cursus. Curabitur mollis mi et euismod vehicula. Nam tincidunt aliquam nunc a ornare. Suspendisse vestibulum laoreet felis bibendum placerat. Integer quam justo, consequat in erat vel, venenatis auctor magna. Donec a leo ut felis congue dictum. Etiam neque leo, tincidunt id ipsum sit amet, euismod rutrum nunc. Vivamus at libero orci.</p>
    </div>
    <div>
      <p>Proin commodo dictum dui. Proin venenatis turpis ac nunc auctor, et suscipit ipsum efficitur. Mauris vulputate neque nec est placerat, ac pharetra metus interdum. Pellentesque vitae nisl semper, vehicula nisi in, gravida massa. Nunc justo ipsum, convallis ut augue in, interdum pretium tortor. Praesent pharetra semper augue ac euismod. Ut non lectus euismod, vehicula ante at, sollicitudin risus. In hac habitasse platea dictumst. In congue elit mi, et dictum risus pulvinar in.</p>
      <p>Integer luctus tellus dui. Nulla eget neque sed massa semper lacinia eu id tortor. Etiam lacinia, nulla sed sodales porttitor, orci quam blandit nulla nec ultricies.</p>
    </div>
  </div>
  <h2 class="section-title" style="top:309px">Timeline</h2>
  <table class="timeline">
    <colgroup><col style="width:111px"><col style="width:153px"><col style="width:79px"></colgroup>
    <thead><tr><th>PHASE</th><th>DESCRIPTION</th><th>END DATE</th></tr></thead>
    <tbody>
      <tr><td>Duis molestie sagittis metus sed cursus. Curabitur mollis mi et euismod vehicula.</td><td>Duis molestie sagittis metus sed cursus. Curabitur mollis mi et euismod vehicula. Donec a leo ut felis congue dictum. Etiam neque leo.</td><td class="date">SEPTEMBER 30,2022</td></tr>
      <tr><td>Duis molestie sagittis metus sed cursus. Curabitur mollis mi et euismod vehicula.</td><td>Duis molestie sagittis metus sed cursus. Curabitur mollis mi et euismod vehicula. Donec a leo ut felis congue dictum. Etiam neque leo.</td><td class="date">SEPTEMBER 30,2022</td></tr>
      <tr><td>Duis molestie sagittis metus sed cursus. Curabitur mollis mi et euismod vehicula.</td><td>Duis molestie sagittis metus sed cursus. Curabitur mollis mi et euismod vehicula. Donec a leo ut felis congue dictum. Etiam neque leo.</td><td class="date">SEPTEMBER 30,2022</td></tr>
    </tbody>
  </table>
  <div class="footer-band"></div>
</section>

<!-- Pricing -->
<section class="page page--pricing">
  <svg class="header__art" width="398" height="86" aria-hidden="true">
    <polygon points="155,0 398,0 398,63 198,63" fill="url(#band)"/>
    <polygon points="184,42 212,85 169,85" fill="#1b5fab"/>
    <line x1="0" y1="85.5" x2="398" y2="85.5" stroke="var(--accent-light)" stroke-width="1"/>
  </svg>
  <div class="brand"><span class="brand__mark"></span>Ridgeline Insulation</div>
  <svg class="brand-bar" width="140" height="7" aria-hidden="true"><polygon points="0,0 140,0 137,7 0,7" fill="url(#barfill)"/></svg>
  <div class="header-contact">
    <div class="contact-line"><svg class="icon" style="color:var(--accent-light)"><use href="#i-pin"/></svg>P.O Box 482, Lakeside Texas 75990</div>
    <div class="contact-line"><svg class="icon" style="color:var(--accent-light)"><use href="#i-phone"/></svg>555-018-2740</div>
    <div class="contact-line"><svg class="icon" style="color:var(--accent-light)"><use href="#i-mail"/></svg>@ridgelinefoam.com</div>
  </div>
  <nav class="nav"><span>SPRAY FOAM</span><span class="sep">|</span><span>FIBERGLASS</span><span class="sep">|</span><span>INSULATION</span><span class="sep">|</span><span>ROOFING</span></nav>
  <h2 class="section-title" style="top:105px">Pricing</h2>
  <div class="pricing">
    <div class="pricing__head"><span class="c-desc">Description</span><span class="c-qty">Quantity</span><span class="c-price">Price</span><span class="c-total">Total</span></div>
    <div class="pricing__rows">
      <div class="pricing__row pricing__row--item"><span class="c-desc">Interview expenses</span><span class="c-qty">20.00</span><span class="c-price">$ 5.00&nbsp; person</span><span class="c-total">$ 100.00</span></div>
      <div class="pricing__row pricing__row--item"><span class="c-desc">Jewelry materials</span><span class="c-qty">5.00</span><span class="c-price">$ 200.00&nbsp; pc</span><span class="c-total">$ 1,000.00</span></div>
      <div class="pricing__row pricing__row--item"><span class="c-desc">Production</span><span class="c-qty">5.00</span><span class="c-price">$ 100.00&nbsp; pc</span><span class="c-total">$ 500.00</span></div>
      <div class="pricing__row pricing__row--item"><span class="c-total">$ 0.00</span></div>
      <div class="pricing__row pricing__row--item"><span class="c-total">$ 0.00</span></div>
      <div class="pricing__row pricing__row--sum"><span class="c-desc">Taxes</span><span class="c-total">0 %</span></div>
      <div class="pricing__row pricing__row--sum"><span class="c-desc">Discount (%)</span><span class="c-total">0 %</span></div>
      <div class="pricing__row pricing__row--grand"><span class="c-desc">Total</span><span class="c-total">$ 1,600.00</span></div>
    </div>
  </div>
  <div class="footer-band"></div>
</section>

</body>
</html>
```